BQN Project Signage

Need a sign to be displayed in the front of properties currently under Construction or Renovation to advertise our company information. Need it to be Professional and Contemporary. We are a Design/Build Construction Company. Information should include Company Name, email, website, phone number. Attached: Logo and company brochure, also included and inspiration images

```html
<!DOCTYPE html>
<html lang="en">
<head>
<meta charset="utf-8">
<title>BQN Construction – Project Sign</title>
<link href="https://fonts.googleapis.com/css2?family=Anton&family=Montserrat:wght@500;600;700&display=swap" rel="stylesheet">
<style>
  :root {
    --page: #f7f7f7;
    --sign-light: #f1f2f3;
    --sign-dark: #0b0b0b;
    --ink: #111111;
    --white: #ffffff;
    --accent: #ece940;
  }
  html, body {
    margin: 0;
    width: 1200px;
    height: 1200px;
    overflow: hidden;
    background: var(--page);
  }
  .sign {
    position: absolute;
    left: 232px;
    top: 49px;
    width: 736px;
    height: 1102px;
    background: linear-gradient(160deg, #e9eaec 0%, var(--sign-light) 40%, #fafafa 100%);
    box-shadow: 0 4px 14px rgba(0,0,0,0.35);
    overflow: hidden;
    font-family: "Montserrat", sans-serif;
  }
  .sign-shapes {
    position: absolute;
    inset: 0;
  }
  .brand-mark {
    position: absolute;
    left: 68px;
    top: 148px;
    display: flex;
    align-items: center;
    gap: 16px;
  }
  .brand-dot {
    width: 40px;
    height: 40px;
    border-radius: 50%;
    background: var(--accent);
  }
  .brand-name {
    font-family: "Montserrat", sans-serif;
    font-weight: 600;
    font-size: 42px;
    letter-spacing: 2px;
    color: var(--ink);
    line-height: 1;
  }
  .headline {
    position: absolute;
    left: 23px;
    top: 395px;
    width: 700px;
    margin: 0;
    font-family: "Anton", sans-serif;
    font-weight: 400;
    color: var(--white);
    font-size: 126px;
    line-height: 130px;
    letter-spacing: 0;
    white-space: nowrap;
  }
  .contact-row {
    position: absolute;
    left: 63px;
    display: flex;
    align-items: center;
    gap: 26px;
    color: var(--white);
    font-size: 38px;
    font-weight: 500;
    letter-spacing: 0.3px;
  }
  .contact-row svg { width: 32px; height: 32px; flex: none; }
  .contact-email { top: 678px; }
  .contact-web { top: 738px; }
  .phone-line {
    position: absolute;
    left: 0;
    width: 736px;
    text-align: center;
    color: var(--white);
    font-size: 50px;
    font-weight: 500;
    line-height: 1;
  }
  .phone-line strong { font-weight: 700; }
  .phone-direct { top: 948px; }
  .phone-office { top: 1034px; }
</style>
</head>
<body>
  <div class="sign">
    <svg class="sign-shapes" viewBox="0 0 736 1102" width="736" height="1102">
      <defs>
        <linearGradient id="darkPanel" x1="0" y1="0" x2="1" y2="1">
          <stop offset="0" stop-color="#2a2a2a"/>
          <stop offset="0.35" stop-color="#0d0d0d"/>
          <stop offset="1" stop-color="#050505"/>
        </linearGradient>
      </defs>
      <polygon class="divider-rule" points="0,350 285,350 736,507 736,520 285,362 0,362" fill="var(--sign-dark)"/>
      <polygon class="dark-panel" points="0,362 285,362 736,520 736,1102 0,1102" fill="url(#darkPanel)"/>
      <g class="phone-badge" stroke="var(--accent)" fill="none" stroke-width="3">
        <line x1="232" y1="878" x2="297" y2="878"/>
        <line x1="426" y1="878" x2="492" y2="878"/>
        <circle cx="360" cy="870" r="43"/>
        <path d="M343 850 l8 -3 l7 14 l-6 5 q5 11 15 16 l5 -6 l14 7 l-3 8 q-4 5 -12 3 q-28 -10 -35 -36 q-1 -6 7 -8z" fill="var(--accent)" stroke="none"/>
        <path d="M365 852 a12 12 0 0 1 12 12 M366 843 a21 21 0 0 1 20 20" stroke-width="3"/>
      </g>
      <rect class="phone-divider" x="93" y="1010" width="550" height="5" fill="var(--accent)"/>
    </svg>

    <div class="brand-mark">
      <span class="brand-dot"></span>
      <span class="brand-name">BQN CONSTRUCTION</span>
    </div>

    <h1 class="headline">BQN<br>Construction</h1>

    <div class="contact-row contact-email">
      <svg viewBox="0 0 32 32" fill="none" stroke="var(--accent)" stroke-width="2.5">
        <rect x="3" y="8" width="26" height="19" rx="2"/>
        <path d="M3 10 l13 10 l13 -10 M3 27 l10 -9 M29 27 l-10 -9"/>
      </svg>
      <span>mara@bqnconstruction.com</span>
    </div>
    <div class="contact-row contact-web">
      <svg viewBox="0 0 32 32" fill="none" stroke="var(--accent)" stroke-width="2.5">
        <circle cx="16" cy="16" r="13"/>
        <ellipse cx="16" cy="16" rx="6" ry="13"/>
        <path d="M3 16 h26 M5 9 h22 M5 23 h22 M16 3 v26"/>
      </svg>
      <span>www.bqnconstruction.com</span>
    </div>

    <div class="phone-line phone-direct">Direct: <strong>555.301.2846</strong></div>
    <div class="phone-line phone-office">Office: <strong>555.308.7190</strong></div>
  </div>
</body>
</html>
```